Vantor Reach needs a Business Card Design

We need a business card design for an Information Technology company based in Fairfax Virginia called Vantor Reach. We want the business card to use our logo colors. We need it to be double-sided. The business card needs to look professional but we would like it to be unique. You can get company information from our web site (http://www.vantorreachllc.example).

Target Market(s)

Target market is Government Agencies and Business Professionals.

Industry/Entity Type

Business

Requirements
Must have
• Must have section for company name, company address, company URL, employee name, title, phone and email. Also must have company logo and space for entering logos.

```html
<!DOCTYPE html>
<html lang="en">
<head>
<meta charset="utf-8">
<title>Vantor Reach — Business Card</title>
<link rel="stylesheet" href="https://fonts.googleapis.com/css2?family=Arimo:wght@700&family=Tinos:wght@700&display=swap">
<style>
  :root{
    --backdrop:#c3e6ec;
    --sky:#2680ff;
    --royal:#1a2ee8;
    --band-top:#3a50ee;
    --band-bottom:#0a1cf0;
    --rule:#232323;
    --paper:#ffffff;
    --ink:#151515;
  }
  *{margin:0;padding:0;box-sizing:border-box}
  html,body{width:1200px;height:900px;overflow:hidden;background:var(--backdrop)}
  .stage{position:relative;width:1200px;height:900px}
  .card{position:absolute;left:274px;width:658px;overflow:hidden;background:var(--paper)}
  .card--back{top:24px;height:412px}
  .card--front{top:466px;height:411px}

  .back-field{position:absolute;left:0;top:0;width:100%;height:273px;background:var(--sky)}
  .rule{position:absolute;left:0;width:100%;height:8px;background:var(--rule)}
  .band{position:absolute;left:0;width:100%;bottom:0;background:linear-gradient(var(--band-top),var(--band-bottom))}
  .card--back .rule{top:284px}
  .card--back .band{top:292px}
  .card--front .rule{top:284px}
  .card--front .band{top:292px}

  .brand-pill{position:absolute;left:137px;top:72px;width:379px;height:71px;background:var(--paper);border-radius:18px;display:flex;align-items:center;justify-content:center;gap:12px}
  .brand{display:flex;align-items:center;gap:12px}
  .brand__mark{width:30px;height:30px;background:var(--royal)}
  .brand__name{font-family:"Arimo",Arial,sans-serif;font-weight:700;font-size:27px;color:var(--royal);letter-spacing:.3px}
  .card--front .brand{position:absolute;left:0;width:100%;top:38px;justify-content:center}

  .detail{position:absolute;font-family:"Tinos","Times New Roman",serif;font-weight:700;color:var(--paper);font-size:17px;line-height:22px}
  .icon{position:absolute}

  .person__name{position:absolute;right:403px;top:122px;font-family:"Tinos","Times New Roman",serif;font-weight:700;font-size:25px;color:var(--sky);white-space:nowrap}
  .person__title{position:absolute;right:404px;top:160px;font-family:"Arimo",Arial,sans-serif;font-weight:700;font-size:14px;color:var(--ink);white-space:nowrap}
  .divider{position:absolute;left:308px;top:114px;width:2px;height:88px;background:var(--sky)}
  .contact{position:absolute;font-family:"Tinos","Times New Roman",serif;font-weight:700;font-size:17px;color:var(--royal);white-space:nowrap}
</style>
</head>
<body>
<main class="stage">

  <section class="card card--back" aria-label="Card back">
    <div class="back-field"></div>
    <div class="brand-pill">
      <div class="brand"><span class="brand__mark"></span><span class="brand__name">Vantor Reach</span></div>
    </div>
    <div class="rule"></div>
    <div class="band">
      <svg class="icon" style="left:30px;top:17px" width="24" height="24" viewBox="0 0 24 24" fill="none" stroke="#fff" stroke-width="1.3">
        <circle cx="12" cy="12" r="10.5"/><ellipse cx="12" cy="12" rx="4.5" ry="10.5"/>
        <line x1="1.5" y1="12" x2="22.5" y2="12"/><path d="M3.5 6.5h17M3.5 17.5h17"/>
      </svg>
      <p class="detail" style="left:76px;top:16px">www.vantorreachllc.example</p>
      <svg class="icon" style="left:30px;top:51px" width="24" height="24" viewBox="0 0 24 24" fill="none" stroke="#fff" stroke-width="1.3">
        <path d="M2 11 12 3l10 8"/><path d="M5 9v13h14V9"/><rect x="8" y="14" width="3" height="3"/><rect x="13" y="14" width="3" height="8"/>
      </svg>
      <p class="detail" style="left:75px;top:52px">1450 Harbor Crest Ave, Suite 210<br>Fairfax, VA 22030</p>
    </div>
  </section>

  <section class="card card--front" aria-label="Card front">
    <div class="brand"><span class="brand__mark"></span><span class="brand__name">Vantor Reach</span></div>
    <p class="person__name">Mr. Daniel Harlow</p>
    <p class="person__title">Senior Executive</p>
    <div class="divider"></div>
    <svg class="icon" style="left:367px;top:130px" width="24" height="24" viewBox="0 0 24 24">
      <rect width="24" height="24" rx="4" fill="var(--royal)"/>
      <path d="M8 5c-1.5.5-2.5 2-2 4 1 4 4 8 8 10 2 .8 3.5 0 4.2-1.4l-2.6-2.2-1.8 1.2c-2-1-3.6-3.2-4.3-5.3l1.7-1.2L10 6.2z" fill="#fff"/>
    </svg>
    <p class="contact" style="left:414px;top:132px">555 014 2876</p>
    <svg class="icon" style="left:368px;top:177px" width="22" height="20" viewBox="0 0 22 20" fill="none" stroke="var(--royal)" stroke-width="1.3">
      <rect x=".8" y=".8" width="20.4" height="18.4"/><path d="M.8 .8 11 11 21.2 .8M.8 19.2l7.5-7.5M21.2 19.2l-7.5-7.5"/>
    </svg>
    <p class="contact" style="left:412px;top:175px">danielharlow@mail.example</p>
    <div class="rule"></div>
    <div class="band">
      <p class="detail" style="left:213px;top:32px">1450 Harbor Crest Ave, Suite 210<br>Fairfax, VA 22030</p>
    </div>
  </section>

</main>
</body>
</html>
```